Veltrix web stylesheet and logo

We are developing a new site for Veltrix and would like someone to provide a new logo and a web page style guide.
This company connects carriers with with customers that need specialty moves: store fixtures, displays, exhibits, technology, manufacturing equipment, etc.
We want to convey quality customer service, quality transportation, and the use of current technology in our business. We do not want to look like a trucking company.
Logo needs a total remake!!!

Target Market(s)

Technology, Retail, Manufacturing, Hospitalty...

Industry/Entity Type

It Company

Logo Text

we will provide some thing soon

Number of Pages Required

1 page

Font styles to use
Serif
Sans Serif

Requirements
Must have
• Warm colors, professional looking.
Nice to have
• If you have pics to include we'll consider
Should not have
• We must no look like a trucking company.

```html
<!DOCTYPE html>
<html lang="en">
<head>
<meta charset="utf-8">
<title>Veltrix — Quality Customer Service</title>
<link rel="stylesheet" href="https://fonts.googleapis.com/css2?family=Roboto+Slab:wght@400;700&family=Open+Sans:wght@400;600;700&display=swap">
<style>
:root{
  --yellow:#f8c21c;
  --yellow-deep:#f0b400;
  --blue:#1e6fd9;
  --dark:#222428;
  --darker:#17181b;
  --ink:#333;
  --muted:#777;
  --light:#f4f4f4;
  --white:#fff;
}
*{box-sizing:border-box;margin:0;padding:0}
html,body{width:1200px;height:2928px;overflow:hidden}
body{position:relative;background:var(--white);font-family:"Open Sans",Arial,sans-serif;color:var(--ink);font-size:11px;line-height:1.6}
.abs{position:absolute}
.slab{font-family:"Roboto Slab",Georgia,serif}
.photo{position:absolute}
.btn{position:absolute;display:flex;align-items:center;justify-content:center;font-size:9px;font-weight:700;letter-spacing:1px;text-transform:uppercase}
.btn-outline{border:1px solid #999;color:var(--ink);background:var(--white)}
.section-title{position:absolute;left:0;width:1200px;text-align:center;font-family:"Roboto Slab",Georgia,serif;font-weight:700;font-size:34px;color:var(--yellow);line-height:1}
.section-sub{position:absolute;left:0;width:1200px;text-align:center;font-size:9px;font-weight:700;letter-spacing:1px;color:var(--ink)}
.section-text{position:absolute;left:350px;width:500px;text-align:center;font-size:10px;color:var(--muted);line-height:1.6}

/* Hero */
.hero{position:absolute;left:0;top:0;width:1200px;height:480px}
.hero-photo{left:0;top:0;width:1200px;height:480px;background:linear-gradient(100deg,#3a3d42 0%,#5b5e63 40%,#4a4c50 70%,#2d2f33 100%)}
.hero-shade{position:absolute;inset:0;background:rgba(20,22,26,.45)}
.nav-bar{position:absolute;left:0;top:0;width:1200px;height:48px}
.logo{position:absolute;left:258px;top:10px;font-family:"Roboto Slab",Georgia,serif;font-weight:700;font-size:22px;color:var(--white);letter-spacing:1px}
.logo-tag{position:absolute;left:258px;top:36px;font-size:7px;color:#ddd;letter-spacing:1px}
.nav{position:absolute;left:520px;top:14px;display:flex;gap:4px;list-style:none}
.nav li{font-size:9px;font-weight:700;color:var(--white);padding:6px 12px;letter-spacing:.5px}
.nav li.active{background:var(--blue)}
.hero-welcome{position:absolute;left:0;width:1200px;top:280px;text-align:center;font-family:"Roboto Slab",Georgia,serif;font-weight:700;font-size:50px;color:var(--yellow);line-height:1}
.hero-title{position:absolute;left:0;width:1200px;top:336px;text-align:center;font-family:"Roboto Slab",Georgia,serif;font-weight:700;font-size:28px;color:var(--white);line-height:1}
.hero-text{position:absolute;left:300px;width:600px;top:374px;text-align:center;font-size:10px;color:#e6e6e6}
.quote-form{position:absolute;left:262px;top:418px;width:676px;height:40px;background:var(--blue);display:flex;align-items:center;gap:10px;padding:0 10px}
.quote-form .field{flex:1;height:24px;background:var(--white);font-size:9px;color:#999;display:flex;align-items:center;padding-left:8px}
.quote-form .submit{width:110px;height:24px;background:var(--yellow);font-size:9px;font-weight:700;color:var(--dark);display:flex;align-items:center;justify-content:center;letter-spacing:1px}

/* About */
.consult-box{position:absolute;left:250px;top:600px;width:222px;height:122px;background:var(--yellow);text-align:center}
.consult-box .small{margin-top:22px;font-size:10px;font-weight:700;color:var(--dark)}
.consult-box .big{font-family:"Roboto Slab",Georgia,serif;font-weight:700;font-size:17px;color:var(--dark);line-height:1.2}
.consult-box .btn{left:72px;top:84px;width:78px;height:20px;background:var(--white);color:var(--dark)}
.consult-text{position:absolute;left:250px;top:738px;width:222px;font-size:10px;color:var(--muted)}
.about-photo{left:492px;top:600px;width:184px;height:180px;background:linear-gradient(135deg,#c9ccd1,#6f747c 60%,#3a3d42)}
.about-heading{position:absolute;left:694px;top:598px;width:260px;font-family:"Roboto Slab",Georgia,serif;font-weight:700;font-size:19px;color:var(--dark);line-height:1.15}
.about-text{position:absolute;left:694px;top:650px;width:260px;font-size:10px;color:var(--muted)}
.about-more{left:694px;top:744px;width:86px;height:22px}

/* Services */
.services-bg{left:0;top:820px;width:1200px;height:568px;background:linear-gradient(110deg,#f2b900 0%,#f7c734 35%,#e9d9a6 55%,#f6c22a 75%,#eeb000 100%)}
.services-tint{position:absolute;left:0;top:820px;width:1200px;height:568px;background:rgba(248,194,28,.55)}
.services .section-title{color:var(--white)}
.services .section-sub{color:var(--white)}
.services .section-text{color:#5a4a12}
.svc-wide{left:250px;top:974px;width:472px;height:188px;background:linear-gradient(120deg,#8e8f8d,#d8d6cf 45%,#a9a7a0)}
.svc-feature{position:absolute;left:722px;top:974px;width:230px;height:188px;background:var(--blue);padding:44px 20px 0 22px;color:var(--white)}
.svc-feature .name{font-family:"Roboto Slab",Georgia,serif;font-weight:700;font-size:15px;letter-spacing:.5px}
.svc-feature .desc{font-size:9px;color:#dbe8fb;margin-top:2px}
.svc-feature .price{font-family:"Roboto Slab",Georgia,serif;font-weight:700;font-size:14px;color:var(--yellow);margin-top:6px}
.svc-a{left:250px;top:1164px;width:228px;height:168px;background:linear-gradient(135deg,#cfd1d4,#8b8f95)}
.svc-b{left:480px;top:1164px;width:240px;height:168px;background:linear-gradient(135deg,#6d6a66,#b7a99a 55%,#4d4945)}
.svc-c{left:722px;top:1164px;width:230px;height:168px;background:linear-gradient(135deg,#c8d4dd,#8ea4b3 60%,#5e6f7c)}
.svc-frame{position:absolute;border:3px solid var(--white)}

/* Store */
.store-photo{left:0;top:1540px;width:600px;height:292px;background:linear-gradient(180deg,#6fa3d6 0%,#b9d6ee 50%,#e7c79a 85%,#c9a16f 100%)}
.band{position:absolute;height:40px;background:var(--yellow);display:flex;align-items:center;justify-content:space-between;font-family:"Roboto Slab",Georgia,serif;font-weight:700;color:var(--dark)}
.band .name{font-size:22px}
.band .price{font-size:13px}
.band-displays{left:620px;top:1552px;width:580px;padding:0 60px 0 20px;clip-path:polygon(14px 0,100% 0,100% 100%,0 100%)}
.band-tech{left:0;top:1848px;width:600px;padding:0 20px 0 250px}
.bullets{position:absolute;list-style:none;font-size:10px;color:var(--muted)}
.bullets li{position:relative;padding-left:14px;margin-bottom:12px}
.bullets li::before{content:"";position:absolute;left:0;top:6px;width:5px;height:5px;background:var(--yellow)}
.bullets-displays{left:660px;top:1608px;width:440px}
.bullets-tech{left:250px;top:1910px;width:330px}
.displays-more{left:660px;top:1744px;width:86px;height:22px}
.tech-more{left:250px;top:2050px;width:86px;height:22px}
.tech-photo{left:600px;top:1848px;width:600px;height:232px;background:linear-gradient(120deg,#e9e4dc,#c7b8a3 50%,#8d7c68);clip-path:polygon(40px 0,100% 0,100% 100%,0 100%)}
.tech-edge{position:absolute;left:600px;top:2076px;width:600px;height:4px;background:var(--yellow)}

/* Testimonials */
.testi-photo{left:0;top:2128px;width:1200px;height:232px;background:linear-gradient(100deg,#2e3034,#46484c 50%,#2a2c30)}
.testi-shade{position:absolute;left:0;top:2128px;width:1200px;height:232px;background:rgba(15,16,18,.55)}
.testimonials .section-title{color:var(--white);top:2170px}
.testi-quote{position:absolute;left:320px;width:560px;top:2222px;text-align:center;font-size:10px;color:#ddd}
.testi-name{position:absolute;left:0;width:1200px;top:2276px;text-align:center;font-size:10px;font-weight:700;color:var(--yellow)}
.testi-role{position:absolute;left:0;width:1200px;top:2292px;text-align:center;font-size:9px;color:#bbb}
.dots{position:absolute;left:576px;top:2318px;display:flex;gap:8px}
.dots span{width:8px;height:8px;border-radius:50%;background:#777}
.dots span.on{background:var(--white)}

/* Contact */
.map{left:0;top:2360px;width:1200px;height:300px;background:linear-gradient(120deg,#f3efe2 0%,#f1e2a8 40%,#f4cf4a 70%,#f0c238 100%)}
.contact-panel{position:absolute;left:250px;top:2366px;width:224px;height:288px;background:var(--yellow);padding:14px 14px}
.contact-panel h3{font-family:"Roboto Slab",Georgia,serif;font-weight:700;font-size:22px;color:var(--white);line-height:1}
.contact-panel .lead{font-size:8px;color:var(--dark);margin:4px 0 10px}
.contact-panel .row{display:flex;gap:6px;margin-bottom:8px}
.contact-panel .input{flex:1;height:22px;background:var(--white);font-size:8px;color:#999;padding:4px 6px}
.contact-panel .area{height:56px}
.contact-panel .send{width:84px;height:22px;margin:8px auto 0;background:var(--blue);color:var(--white);font-size:9px;font-weight:700;display:flex;align-items:center;justify-content:center;letter-spacing:1px}
.map-pin{position:absolute;left:678px;top:2398px}

/* Footer */
.footer{position:absolute;left:0;top:2660px;width:1200px;height:240px;background:var(--dark)}
.foot-col{position:absolute;top:2676px;width:170px;font-size:9px;color:#aaa;line-height:1.55}
.foot-col h4{font-family:"Roboto Slab",Georgia,serif;font-weight:700;font-size:14px;color:var(--white);margin-bottom:8px}
.foot-col .hl{color:var(--yellow)}
.foot-col p{margin-bottom:8px}
.foot-brand{left:250px}
.foot-tweets{left:428px}
.foot-contact{left:606px}
.foot-news{left:784px}
.contact-line{display:flex;align-items:center;gap:6px;margin-bottom:6px}
.news-row{display:flex;margin-top:4px}
.news-row .input{flex:1;height:22px;background:var(--white);font-size:8px;color:#999;padding:4px 6px}
.news-row .go{width:48px;height:22px;background:var(--yellow);color:var(--dark);font-size:8px;font-weight:700;display:flex;align-items:center;justify-content:center}
.social{display:flex;gap:10px;margin-top:22px}
.social span{width:34px;height:34px;border-radius:50%;background:var(--yellow)}
.bottom-bar{position:absolute;left:0;top:2900px;width:1200px;height:28px;background:var(--yellow);font-size:8px;color:var(--dark)}
.bottom-bar .left{position:absolute;left:250px;top:8px}
.bottom-bar .right{position:absolute;right:250px;top:8px}
</style>
</head>
<body>

<!-- Hero -->
<header class="hero">
  <div class="photo hero-photo" role="img" aria-label="Business team meeting in a bright modern office"></div>
  <div class="hero-shade"></div>
  <div class="nav-bar">
    <div class="logo">VELTRIX</div>
    <div class="logo-tag">SPECIALTY MOVES</div>
    <ul class="nav">
      <li class="active">HOME</li><li>ABOUT US</li><li>STORE</li><li>SERVICE</li><li>TESTIMONIAL</li><li>CONTACT US</li>
    </ul>
  </div>
  <div class="hero-welcome">WELCOME TO</div>
  <div class="hero-title">VELTRIX QUALITY CUSTOMER SERVICE</div>
  <p class="hero-text">Specialty moves handled with care by trusted carriers, matched to your schedule and budget every single time you ship.</p>
  <div class="quote-form">
    <div class="field">Your Name</div>
    <div class="field">Email Address</div>
    <div class="field">Phone</div>
    <div class="submit">SUBMIT</div>
  </div>
</header>

<!-- About -->
<section class="about">
  <div class="section-title" style="top:510px">ABOUT US</div>
  <div class="section-sub" style="top:550px">VELTRIX</div>
  <p class="section-text" style="top:566px">We connect careful carriers with customers who need special handling.</p>
  <div class="consult-box">
    <div class="small">GET YOUR</div>
    <div class="big">FREE CONSULTING</div>
    <div class="btn">LEARN MORE</div>
  </div>
  <p class="consult-text">We plan every move from pickup to delivery so your fixtures and displays arrive ready to install on time.</p>
  <div class="photo about-photo" role="img" aria-label="Colleagues shaking hands across a desk"></div>
  <div class="about-heading">CUSTOMER SERVICE<br>QUALITY</div>
  <p class="about-text">Our coordinators stay with your shipment from the first call to final placement. We match each job with a carrier that knows the cargo, track progress in real time and keep you informed, so store fixtures, exhibits and equipment move safely without surprises.</p>
  <div class="btn btn-outline about-more">READ MORE</div>
</section>

<!-- Services -->
<section class="services">
  <div class="photo services-bg" role="img" aria-label="Delivery drone flying over a warm golden backdrop"></div>
  <div class="services-tint"></div>
  <div class="section-title" style="top:856px">SERVICES</div>
  <div class="section-sub" style="top:894px">VELTRIX</div>
  <p class="section-text" style="top:912px">Dedicated moves for retail, technology, manufacturing and hospitality, planned by specialists and carried out by vetted carriers with the right gear for delicate loads.</p>
  <div class="photo svc-wide" role="img" aria-label="Security cameras mounted on a wall"></div>
  <div class="svc-feature">
    <div class="name">MANUFACTURING</div>
    <div class="desc">Heavy equipment moved with care</div>
    <div class="price">$35.00</div>
  </div>
  <div class="photo svc-a" role="img" aria-label="Laptop on a clean white desk"></div>
  <div class="photo svc-b" role="img" aria-label="Engineer wearing smart glasses"></div>
  <div class="photo svc-c" role="img" aria-label="Quadcopter drone hovering in the sky"></div>
  <div class="svc-frame" style="left:720px;top:972px;width:234px;height:192px;border-color:var(--blue)"></div>
</section>

<!-- Store -->
<section class="store">
  <div class="section-title" style="top:1424px">STORE</div>
  <div class="section-sub" style="top:1462px">VELTRIX</div>
  <p class="section-text" style="top:1480px">Choose the service that fits your project. Each package includes planning, careful loading, tracked transport and placement on site by crews trained for sensitive goods and tight schedules.</p>

  <div class="photo store-photo" role="img" aria-label="Camera drone flying above a desert landscape"></div>
  <div class="band band-displays"><span class="name">DISPLAYS</span><span class="price">$395.00</span></div>
  <ul class="bullets bullets-displays">
    <li>Retail displays and store fixtures wrapped, crated and delivered straight to the sales floor for fast setup.</li>
    <li>Exhibit booths moved to trade shows and events with on-time arrival and careful handling throughout.</li>
    <li>Signage and showcases installed by crews who understand finishes, glass and fragile lighting parts.</li>
  </ul>
  <div class="btn btn-outline displays-more">READ MORE</div>

  <div class="band band-tech"><span class="name">TECHNOLOGY</span><span class="price">$350.00</span></div>
  <ul class="bullets bullets-tech">
    <li>Servers, kiosks and screens packed with static safe material and moved in climate controlled trucks.</li>
    <li>White glove delivery for sensitive electronics with live tracking from pickup to final placement.</li>
    <li>Setup teams connect and test equipment on arrival so your systems are ready to run that day.</li>
  </ul>
  <div class="btn btn-outline tech-more">READ MORE</div>
  <div class="photo tech-photo" role="img" aria-label="Person wearing a virtual reality headset"></div>
  <div class="tech-edge"></div>
</section>

<!-- Testimonials -->
<section class="testimonials">
  <div class="photo testi-photo" role="img" aria-label="Dim office interior behind a dark overlay"></div>
  <div class="testi-shade"></div>
  <div class="section-title">TESTIMONIALS</div>
  <p class="testi-quote">Our store rollout covered forty locations in six weeks and every fixture arrived on time and undamaged. The team kept us updated at each step and solved problems before we even noticed them.</p>
  <div class="testi-name">Dana Morrow</div>
  <div class="testi-role">Retail Operations Lead</div>
  <div class="dots"><span class="on"></span><span></span><span></span></div>
</section>

<!-- Contact -->
<section class="contact">
  <div class="photo map" role="img" aria-label="Street map of the city around the office location"></div>
  <svg class="map-pin" width="28" height="38" viewBox="0 0 28 38" aria-hidden="true">
    <path d="M14 1C7 1 1.5 6.5 1.5 13.5 1.5 23 14 37 14 37s12.5-14 12.5-23.5C26.5 6.5 21 1 14 1z" fill="#e84c3d"/>
    <circle cx="14" cy="13.5" r="5" fill="#fff"/>
  </svg>
  <div class="contact-panel">
    <h3>CONTACT US</h3>
    <div class="lead">Tell us about your next move</div>
    <div class="row"><div class="input">Name</div><div class="input">Email</div></div>
    <div class="row"><div class="input">Phone Number</div></div>
    <div class="row"><div class="input">Subject</div></div>
    <div class="row"><div class="input area">Message</div></div>
    <div class="send">SEND</div>
  </div>
</section>

<!-- Footer -->
<footer>
  <div class="footer"></div>
  <div class="foot-col foot-brand">
    <h4>VELTRIX</h4>
    <p>Veltrix links quality carriers with businesses that need specialty moves for fixtures, exhibits, technology and equipment, handled with care and backed by real people who answer the phone.</p>
  </div>
  <div class="foot-col foot-tweets">
    <h4>Recent Tweets</h4>
    <p>New tracking dashboard is live for all customers this week. <span class="hl">2 days ago</span></p>
    <p>Exhibit season is here, book your booth moves early. <span class="hl">5 days ago</span></p>
    <p>Forty store rollout finished ahead of schedule. <span class="hl">1 week ago</span></p>
  </div>
  <div class="foot-col foot-contact">
    <h4>Contact Us</h4>
    <div class="contact-line">
      <svg width="12" height="12" viewBox="0 0 12 12" aria-hidden="true"><path d="M6 .5C3.8.5 2 2.3 2 4.5 2 7.5 6 11.5 6 11.5s4-4 4-7C10 2.3 8.2.5 6 .5z" fill="#f8c21c"/><circle cx="6" cy="4.5" r="1.5" fill="#222428"/></svg>
      <span>240 Harbor Lane, Suite 12</span>
    </div>
    <div class="contact-line">
      <svg width="12" height="12" viewBox="0 0 12 12" aria-hidden="true"><path d="M2.5 1h2l1 2.5-1.3.9a6 6 0 0 0 3.4 3.4l.9-1.3 2.5 1v2c0 .6-.5 1-1 1A9 9 0 0 1 1.5 2c0-.5.4-1 1-1z" fill="#f8c21c"/></svg>
      <span>(555) 014-2288</span>
    </div>
    <div class="contact-line">
      <svg width="12" height="12" viewBox="0 0 12 12" aria-hidden="true"><rect x="1" y="2.5" width="10" height="7" fill="#f8c21c"/><path d="M1 2.5l5 4 5-4" fill="none" stroke="#222428" stroke-width="1"/></svg>
      <span>hello@veltrix-moves.com</span>
    </div>
  </div>
  <div class="foot-col foot-news">
    <h4>Newsletter Signup</h4>
    <p>Get service news and shipping tips in your inbox once a month.</p>
    <div class="news-row"><div class="input">Email</div><div class="go">JOIN</div></div>
    <div class="social"><span></span><span></span><span></span></div>
  </div>
  <div class="bottom-bar">
    <span class="left">Copyright 2024 Veltrix. All Rights Reserved.</span>
    <span class="right">Designed for Veltrix specialty moves</span>
  </div>
</footer>

</body>
</html>
```